Flyer Vacation Gift Certificate

I need to create a beautiful flyer 8.5 x 11 PDF format flyer design. <br/><br/>Instructions:<br/>The flyer will really be a gift voucher for a las vegas vacation getaway. So must have a Las Vegas Theme exciting fun<br/><br/>The voucher should have two modules that will be editable. <br/>Must have a "Compliments Of" area and also must have an "Exclusively For" area<br/><br/>Keep in mind that this flyer will be printed so keep that in mind :)<br/><br/>Here the is the content for the vacation voucher:<br/><br/>There is no doubt that Las Vegas is one of the hottest travel destinations around the world. In fact, some people would even go as far as<br/>saying that perhaps it is THE hottest place to visit. Enjoy up to 4 nights of resort/casino accommodations in exciting Las Vegas, NV. Millions of people travel to this exciting city each year to enjoy its thrills. Thanks to the business you received this certificate from, now you can enjoy exciting Las Vegas, NV too!<br/><br/>Features:<br/>*Travel 7 Days A Week<br/>*Stay Your Choice Of Nights (1-4 Nights)<br/>*Good For Two Adults & Two Children<br/>*Pay Just The Taxes & Fees<br/>*Multiple Travel Date Requests Allowed<br/>*Fully Transferable To Another Person<br/>*Just A 30 Days Advance Notice Required<br/>*You Will Have 12 Months To Complete Travel After Redemption<br/><br/>HOW CAN WE DO THIS?<br/><br/>We contract with the world leading hotel chains and resorts to help them fill their otherwise empty rooms.<br/><br/>We help fill empty rooms which the hotels, resorts and cruise lines turn into additional revenue from other areas of their property and future bookings.<br/><br/>Hotels rarely experience full occupancy, yet they remain open, providing rooms and services at fixed costs. So when hotels give out their rooms by partnering with marketing companies like us, they might miss out on the room fee, but they already didn't have that in the first place, at least now they have the opportunity to gain a customer for their in-house restaurants, room service, their casinos, an extra day stay, future bookings, etc.<br/><br/>VIEW ALL THE DETAILS OF THIS SPECIAL OFFER AND REDEEM ONLINE AT <br/>WWW.TOPAZVOUCHERDESK.COM<br/><br/>Certificate ID # 47261-38504<br/>Expires 02/29/2020<br/><br/><br/>*terms and conditions apply see website for details<br/><br/>KEEP IN MIND THE EXAMPLES I AM UPLOADING ARE SIMPLY TO SHOW YOU THAT THEY CONTAIN THE "COMPLIMENTS OF" AND "EXCLUSIVELY FOR" ELEMENTS. THESE MUST BE INCLUDED IN NEW DESIGN. PLEASE ONLY USE THE CONTENT I PROVIDED IN BRIEF, DONT USE CONTENT FROM EXAMPLES.

Target Market(s)

CONSUMERS THAT HAVE BEEN REWARDED WITH A VACATION CERTIFICATE FOR DOING BUSINESS WITH A COMPANY.

COMPANIES USE THESE AS MARKETING INCENTIVES TO ATTRACT MORE CUSTOMERS AND TO REWARD LOYALTY, ETC.

Industry/Entity Type

Travel Industry

Colors

Designer to choose colors to be used in the design.

Requirements
Must have
• I need to create a beautiful flyer 8.5 x 11 PDF format flyer design.
• Instructions:
• The flyer will really be a gift voucher for a las vegas vacation getaway. So must have a Las Vegas Theme exciting fun
• The voucher should have two modules that will be editable.
• Must have a "Compliments Of" area and also must have an "Exclusively For" area
• Keep in mind that this flyer will be printed so keep that in mind :)
• Here the is the content for the vacation voucher:
• There is no doubt that Las Vegas is one of the hottest travel destinations around the world. In fact, some people would even go as far as
• saying that perhaps it is THE hottest place to visit. Enjoy up to 4 nights of resort/casino accommodations in exciting Las Vegas, NV. Millions of people travel to this exciting city each year to enjoy its thrills. Thanks to the business you received this certificate from, now you can enjoy exciting Las Vegas, NV too!
• Features:
• *Travel 7 Days A Week
• *Stay Your Choice Of Nights (1-4 Nights)
• *Good For Two Adults & Two Children
• *Pay Just The Taxes & Fees
• *Multiple Travel Date Requests Allowed
• *Fully Transferable To Another Person
• *Just A 30 Days Advance Notice Required
• *You Will Have 12 Months To Complete Travel After Redemption
• HOW CAN WE DO THIS?
• We contract with the world leading hotel chains and resorts to help them fill their otherwise empty rooms.
• We help fill empty rooms which the hotels, resorts and cruise lines turn into additional revenue from other areas of their property and future bookings.
• Hotels rarely experience full occupancy, yet they remain open, providing rooms and services at fixed costs. So when hotels give out their rooms by partnering with marketing companies like us, they might miss out on the room fee, but they already didn't have that in the first place, at least now they have the opportunity to gain a customer for their in-house restaurants, room service, their casinos, an extra day stay, future bookings, etc.
• VIEW ALL THE DETAILS OF THIS SPECIAL OFFER AND REDEEM ONLINE AT
• WWW.TOPAZVOUCHERDESK.COM
• Certificate ID # 47261-38504
• Expires 02/29/2020
• *terms and conditions apply see website for details
• KEEP IN MIND THE EXAMPLES I AM UPLOADING ARE SIMPLY TO SHOW YOU THAT THEY CONTAIN THE "COMPLIMENTS OF" AND "EXCLUSIVELY FOR" ELEMENTS. THESE MUST BE INCLUDED IN NEW DESIGN. PLEASE ONLY USE THE CONTENT I PROVIDED IN BRIEF, DONT USE CONTENT FROM EXAMPLES.
Nice to have
• EXCITING LAS VEGAS IMAGES THAT MAKE SOMEONE WANT TO GO THERE

```html
<!DOCTYPE html>
<html lang="en">
<head>
<meta charset="utf-8">
<title>Las Vegas Vacation Gift Certificate</title>
<link href="https://fonts.googleapis.com/css2?family=Montserrat:wght@400;500;600;800&display=swap" rel="stylesheet">
<style>
:root{
  --stage:#3a3a3c;
  --paper:#ffffff;
  --blue:#4a7cb5;
  --blue-title:#3f76b5;
  --ink:#1f1f1f;
  --muted:#6a6a6a;
  --panel-light:#ebecef;
  --panel-mid:#d1d2d4;
}
*{box-sizing:border-box;margin:0;padding:0}
html,body{width:969px;height:1200px;overflow:hidden}
body{background:var(--stage);font-family:'Montserrat',sans-serif;color:var(--ink);position:relative}
.flyer{position:absolute;left:92px;top:92px;width:785px;height:1015px;background:var(--paper);overflow:hidden}
.hero{position:absolute;left:0;top:0;width:785px;height:282px;
  background:linear-gradient(180deg,#2c3f66 0%,#4b5c7e 30%,#8a7660 52%,#b98a45 66%,#4a3626 85%,#1e2230 100%)}
.sponsor-card{position:absolute;left:544px;top:0;width:216px;height:185px;background:var(--paper);text-align:center;padding-top:17px}
.sponsor-card .title{color:var(--blue-title);font-weight:500;font-size:16.5px;line-height:19px;letter-spacing:.3px}
.sponsor-card .brand{margin-top:14px;display:flex;align-items:center;justify-content:center;gap:6px;color:var(--blue-title);font-weight:600;font-size:15px}
.sponsor-card .brand i{display:block;width:12px;height:12px;background:var(--blue-title)}
.sponsor-card .brand-sub{color:var(--blue-title);font-weight:600;font-size:7px;letter-spacing:.6px;margin-top:2px}
.sponsor-card .courtesy{margin-top:14px;font-size:13.5px}
.sponsor-card .line{font-size:13px;margin-top:6px}
.sponsor-card .line + .line{margin-top:3px}
.intro{position:absolute;left:0;top:282px;width:785px;height:78px;background:var(--blue);color:#fff;
  font-size:9.9px;line-height:12.4px;text-align:center;padding:12px 28px 0}
.tab{position:absolute;left:0;width:280px;height:35px}
.tab svg{position:absolute;left:0;top:0}
.tab span{position:absolute;left:24px;top:0;line-height:35px;color:#fff;font-weight:800;font-size:14.5px;letter-spacing:.2px}
.tab-how{top:375px}
.tab-features{top:529px}
.tab-terms{top:643px}
.body-copy{position:absolute;left:24px;top:419px;width:740px;font-size:11.2px;line-height:13.9px}
.features{position:absolute;top:572px;list-style:none;font-size:11.5px;line-height:14px}
.features li{position:relative;padding-left:12px}
.features li::before{content:"";position:absolute;left:0;top:5px;width:4px;height:4px;border-radius:50%;background:var(--blue)}
.features-left{left:24px}
.features-right{left:284px;top:571px}
.terms-note{position:absolute;left:25px;top:690px;width:375px;font-size:6.6px;line-height:9px;color:var(--muted)}
.redeem{position:absolute;left:423px;top:643px;width:362px;height:123px}
.redeem svg{position:absolute;left:0;top:0}
.redeem .text{position:absolute;right:48px;top:25px;text-align:right;color:#fff;font-size:11.4px;line-height:14px}
.redeem .text strong{display:block;font-weight:800}
.redeem .text .gap{height:13px}
.module{position:absolute;font-size:13px;font-weight:500;letter-spacing:.4px}
.module-from{left:0;top:751px;width:375px;height:264px;background:var(--panel-light);padding:22px 0 0 24px}
.module-for{left:402px;top:791px;width:383px;height:224px;background:var(--panel-mid);text-align:center;padding-top:18px}
.notch{position:absolute;left:375px;top:751px}
</style>
</head>
<body>
<main class="flyer">
  <div class="hero" role="img" aria-label="Night view of the Las Vegas Strip with lit resorts, fountains and city lights"></div>

  <section class="sponsor-card">
    <p class="title">THIS CERTIFICATE IS<br>COMPLIMENTS OF</p>
    <div class="brand"><i></i>Beacon Reach Pro</div>
    <p class="brand-sub">by brightlanemarketing.com</p>
    <p class="courtesy">Certificate Courtesy Of</p>
    <p class="line">Text Line 2</p>
    <p class="line">Text Line 3</p>
  </section>

  <p class="intro">There is no doubt that Las Vegas is one of the hottest travel destinations around the world. In fact, some people would even go as far as saying that perhaps it is THE hottest place to visit. Enjoy up to 4 nights of resort/casino accommodations in exciting Las Vegas, NV. Millions of people travel to this exciting city each year to enjoy its thrills. Thanks to the business you received this certificate from, now you can enjoy exciting Las Vegas, NV too!</p>

  <div class="tab tab-how">
    <svg width="280" height="35"><polygon points="0,0 262,0 280,17.5 262,35 0,35" fill="var(--blue)"/></svg>
    <span>HOW CAN WE DO THIS?</span>
  </div>
  <div class="body-copy">
    <p>We contract with the world leading hotel chains and resorts to help them fill their otherwise empty rooms. We help fill empty rooms which the hotels, resorts and cruise lines turn into additional revenue from other areas of their property and future bookings.</p>
    <p>Hotels rarely experience full occupancy, yet they remain open, providing rooms and services at fixed costs. So when hotels give out their rooms by partnering with marketing companies like us, they might miss out on the room fee, but they already didn't have that in the first place, at least now they have the opportunity to gain a customer for their in-house restaurants, room service, their casinos, an extra day stay, future bookings, etc.</p>
  </div>

  <div class="tab tab-features">
    <svg width="280" height="35"><polygon points="0,0 262,0 280,17.5 262,35 0,35" fill="var(--blue)"/></svg>
    <span>FEATURES:</span>
  </div>
  <ul class="features features-left">
    <li>Travel 7 Days A Week</li>
    <li>Stay Your Choice Of Nights (1-4 Nights)</li>
    <li>Good For Two Adults &amp; Two Children</li>
    <li>Pay Just The Taxes &amp; Fees</li>
  </ul>
  <ul class="features features-right">
    <li>Multiple Travel Date Requests Allowed</li>
    <li>Fully Transferable To Another Person</li>
    <li>Just A 30 Days Advance Notice Required</li>
    <li>You Will Have 12 Months To Complete Travel After Redemption</li>
  </ul>

  <div class="tab tab-terms">
    <svg width="280" height="35"><polygon points="0,0 262,0 280,17.5 262,35 0,35" fill="var(--blue)"/></svg>
    <span>TERMS AND CONDITIONS</span>
  </div>
  <p class="terms-note">KEEP IN MIND THE EXAMPLES I AM UPLOADING ARE SIMPLY TO SHOW YOU THAT THEY CONTAIN THE "COMPLIMENTS OF"AND"EXCLUSIVELY FOR"ELEMENTS. THESE MUST BE INCLUDED IN NEW DESIGN. PLEASE ONLY USE THE CONTENT I PROVIDED IN BRIEF, DONT USE CONTENT FROM EXAMPLES.</p>

  <aside class="redeem">
    <svg width="362" height="123"><polygon points="61,0 362,0 362,123 61,123 0,61.5" fill="var(--blue)"/></svg>
    <div class="text">
      VIEW ALL THE DETAILS OF THIS SPECIAL<br>OFFER AND REDEEM ONLINE AT
      <div class="gap"></div>
      <strong>WWW.TOPAZVOUCHERDESK.COM</strong>
      <strong>Certificate ID # 47261-38504</strong>
      <strong>Expires 02/29/2020</strong>
    </div>
  </aside>

  <section class="module module-from">COMPLIMENTS OF</section>
  <svg class="notch" width="27" height="264"><polygon points="0,0 27,40 27,264 0,264" fill="var(--stage)"/></svg>
  <section class="module module-for">EXCLUSIVELY FOR</section>
</main>
</body>
</html>
```